Corporate brochure design 4 pages

Hi,

We are a real estate company based in Europe.

We have almost finalized a rebranding.

We are developing a brand book guidelines (still on working process) to help you undertstand the look and feel of our new CI. I would like to receive proposals of design for a corporate brochure template. I need to receive the Indesign files with full ownership rights to be able to adapt all our documentation with this template.
Regarding the images, you can take gabaris on www.pelvaromedia.com. I will be able to take them afterwards.

There will be 4 pages. you will receive the 4 pages on pdf for your consideration with our (almost) actual layout.

- 1st page: cover
- 2nd page: company presentation in french and english
- 3rd page: some market data + graph
- 4th page: 2 retail centers presentation.

In the template, i need to have:
- the paragraph styles in order
- 2 different masters with top/bottom/page number aso.

Please feel free to ask any other questions.

best regards,
Updates

I would like to precise tha t we are active on the commercial real estate sector:

- office transactions (rent /sales)
- property management of administrative and business buildings
- Valuation of properties
- Capital markets (investment advices for selling building)

Industry/Entity Type

Real Estate

Colors

Designer to choose colors to be used in the design.

```html
<!DOCTYPE html>
<html lang="fr">
<head>
<meta charset="utf-8">
<title>Corvane – Corporate brochure</title>
<link href="https://fonts.googleapis.com/css2?family=Roboto+Condensed:ital,wght@0,300;0,400;0,700;1,300;1,400&display=swap" rel="stylesheet">
<style>
  :root {
    --orange: #f26522;
    --charcoal: #231f20;
    --grey-text: #8a8a8a;
    --paper: #ffffff;
    --backdrop: #ececec;
    --photo-warm-a: #e07a3a;
    --photo-warm-b: #5a2a12;
    --photo-cool-a: #2f8fc4;
    --photo-cool-b: #1c2a44;
    --photo-team-a: #d9dde2;
    --photo-team-b: #6f747c;
  }
  * { margin: 0; padding: 0; box-sizing: border-box; }
  html, body { width: 1200px; height: 904px; overflow: hidden; }
  body {
    background: var(--backdrop);
    font-family: "Roboto Condensed", "Arial Narrow", sans-serif;
    position: relative;
  }

  /* ---------- Cover ---------- */
  .cover {
    position: absolute; left: 40px; top: 64px;
    width: 555px; height: 776px;
    background: var(--paper);
    box-shadow: 0 2px 10px rgba(0,0,0,.12);
    overflow: hidden;
  }
  .cover-art { position: absolute; inset: 0; }
  .cover-brand {
    position: absolute; right: 34px; top: 395px; text-align: right;
  }
  .cover-brand .brand-name {
    font-weight: 700; font-size: 74px; line-height: .9;
    color: var(--paper); letter-spacing: -1px;
  }
  .cover-brand .brand-tagline {
    font-weight: 300; font-size: 17.5px; letter-spacing: 3.2px;
    color: var(--orange); margin-top: 4px;
  }
  .cover-url {
    position: absolute; right: 30px; bottom: 34px;
    font-weight: 400; font-size: 13px; letter-spacing: 1.6px;
    color: var(--paper); white-space: nowrap;
  }

  /* ---------- Inside page ---------- */
  .page {
    position: absolute; left: 700px; top: 142px;
    width: 440px; height: 620px;
    background: var(--paper);
    box-shadow: 0 2px 10px rgba(0,0,0,.12);
    overflow: hidden;
  }
  .page-header { position: absolute; left: 0; top: 0; width: 440px; height: 64px; }
  .section-label {
    position: absolute; right: 22px; top: 26px;
    font-size: 10.5px; color: var(--orange); letter-spacing: .3px;
  }
  .section-label em { color: var(--paper); font-style: italic; }

  .heading {
    position: absolute; text-align: right;
    font-weight: 300; font-size: 23px; color: var(--orange);
    letter-spacing: .3px;
  }
  .heading-rule {
    position: absolute; height: 3px; background: var(--orange);
  }
  .body-copy {
    position: absolute; font-weight: 300; font-size: 8.6px; line-height: 1.38;
    color: var(--grey-text); text-align: justify;
  }
  .body-copy p + p { margin-top: 9px; }
  .body-copy.en { font-style: italic; }
  .lead {
    position: absolute; font-weight: 400; font-size: 10.6px; line-height: 1.3;
    color: var(--orange);
  }
  .lead.right { text-align: right; }

  .team-photo {
    position: absolute; left: 232px; top: 178px; width: 186px; height: 138px;
    background: linear-gradient(160deg, var(--photo-team-a) 0%, #b9bec5 45%, var(--photo-team-b) 100%);
  }
  .photo-caption {
    position: absolute; left: 232px; top: 326px;
    font-size: 5.6px; font-style: italic; font-weight: 300; color: #b5b5b5;
  }

  .page-footer-brand {
    position: absolute; left: 22px; top: 572px;
  }
  .page-footer-brand .brand-name {
    font-weight: 700; font-size: 15px; line-height: 1; color: var(--charcoal);
  }
  .page-footer-brand .brand-tagline {
    font-size: 4.6px; letter-spacing: .9px; color: var(--orange); margin-top: 1px;
  }
  .page-footer-bar {
    position: absolute; left: 140px; top: 600px; width: 300px; height: 20px;
    background: var(--orange);
  }
  .page-number {
    position: absolute; right: 22px; top: 6px;
    font-size: 6px; color: var(--paper); letter-spacing: .4px;
  }
  .page-number b { font-weight: 700; font-size: 7px; }
</style>
</head>
<body>

<section class="cover">
  <svg class="cover-art" width="555" height="776" viewBox="0 0 555 776" xmlns="http://www.w3.org/2000/svg">
    <defs>
      <linearGradient id="warmCity" x1="0" y1="0" x2="0.4" y2="1">
        <stop offset="0" stop-color="var(--photo-warm-b)"/>
        <stop offset=".45" stop-color="var(--photo-warm-a)"/>
        <stop offset="1" stop-color="#7a3614"/>
      </linearGradient>
      <linearGradient id="coolCity" x1="0" y1="0" x2="0.2" y2="1">
        <stop offset="0" stop-color="#2f6fb0"/>
        <stop offset=".5" stop-color="var(--photo-cool-a)"/>
        <stop offset="1" stop-color="var(--photo-cool-b)"/>
      </linearGradient>
    </defs>
    <g role="img" aria-label="Warm-toned photograph of city office towers at dusk">
      <polygon points="0,44 176,44 186,250 121,345 0,345" fill="url(#warmCity)"/>
    </g>
    <g role="img" aria-label="Photograph of glass skyscrapers against a blue evening sky">
      <polygon points="196,0 555,0 555,345 139,345 205,250" fill="url(#coolCity)"/>
    </g>
    <rect class="cover-band" x="0" y="345" width="555" height="152" fill="var(--charcoal)"/>
    <rect class="cover-base" x="0" y="500" width="555" height="276" fill="var(--orange)"/>
    <polygon class="cover-slash" points="222,500 240,500 300,776 282,776" fill="var(--paper)"/>
  </svg>

  <div class="cover-brand">
    <div class="brand-name">CORVANE</div>
    <div class="brand-tagline">COMMERCIAL REAL ESTATE</div>
  </div>
  <div class="cover-url">WWW.CORVANE-ESTATE.COM</div>
</section>

<section class="page">
  <svg class="page-header" width="440" height="64" viewBox="0 0 440 64" xmlns="http://www.w3.org/2000/svg">
    <g role="img" aria-label="Photograph of a warm-toned building facade">
      <polygon points="0,0 122,0 122,64 0,64" fill="url(#warmCity)"/>
    </g>
    <g role="img" aria-label="Photograph of a curved blue glass office building">
      <polygon points="130,0 250,0 236,64 130,64" fill="url(#coolCity)"/>
    </g>
    <polygon points="258,0 440,0 440,64 244,64" fill="var(--charcoal)"/>
  </svg>
  <div class="section-label">A PROPOS DE NOUS/<em>ABOUT US</em></div>

  <h2 class="heading" style="left:30px; top:100px; width:180px;">UNE ÉQUIPE</h2>
  <div class="heading-rule" style="left:30px; top:131px; width:182px;"></div>
  <div class="body-copy fr" style="left:30px; top:150px; width:182px;">
    <p>Notre connaissance du marché luxembourgeois, nos compétences et notre engagement dans les missions qui nous sont confiées font de Meridia Partners l'acteur majeur de l'immobilier d'entreprise au Grand-Duché. Nous sommes fiers de cette position et nous travaillons tous les jours pour la conserver.</p>
    <p>Viser l'excellence suppose de savoir améliorer sans cesse nos prestations pour répondre le plus précisément à vos besoins. Venez nous consulter, vous constaterez que nos collaborateurs prennent le temps de vous écouter pour bien comprendre votre demande. Leur professionnalisme, leur savoir-faire et leur mobilisation nous permettront de trouver la solution.</p>
  </div>

  <p class="lead" style="left:232px; top:98px; width:186px;">Proposer des services de qualité répondant parfaitement à vos attentes est notre ambition. Elle est partagée par tous les membres de notre équipe.</p>
  <div class="team-photo" role="img" aria-label="Group photograph of the four partners in business suits"></div>
  <div class="photo-caption">Luc Almeras, Pierre Dovel, Marc Sentis, Henri Valmont.</div>

  <h2 class="heading" style="left:30px; top:383px; width:180px;">A TEAM</h2>
  <div class="heading-rule" style="left:30px; top:414px; width:182px;"></div>
  <p class="lead right" style="left:30px; top:428px; width:182px;">Our ambition is to offer quality services that perfectly meet your expectations. This ambition is shared by all members of the team.</p>

  <div class="body-copy en" style="left:232px; top:382px; width:186px;">
    <p>Thanks to our knowledge of the Luxembourg market, our skills and our commitment to the missions entrusted to us, Meridia Partners is the undisputed leader in commercial real estate in the Grand Duchy. We are proud of this position and work hard to deserve it every day.</p>
    <p>Targeting excellence means the constant improvement of our services in order to more accurately meet your needs. When you meet with us, you will find that our employees take the necessary time to listen to you and to correctly understand your need. Their professionalism, know-how and mobilisation will ensure that we find the right solution.</p>
  </div>

  <div class="page-footer-brand">
    <div class="brand-name">CORVANE</div>
    <div class="brand-tagline">COMMERCIAL REAL ESTATE</div>
  </div>
  <div class="page-footer-bar">
    <span class="page-number">PAGE <b>2</b></span>
  </div>
</section>

</body>
</html>
```